Kentucky residential recovery center needs a flyer design

We need a flyer design for a 16 bed male residential/inpatient recovery center based in Richmond, Kentucky. The facility provides short term (average 30 day) treatment to those struggling with substace abuse and addiction. The design should communicate trust, assurance, safety.
Our wesite provides more information https://morvalcare.org/treatment-services/residential-treatment/

Target Market(s)

Men (typically 30-50) struggling with substance addiction

```html
<!DOCTYPE html>
<html lang="en">
<head>
<meta charset="utf-8">
<title>Morval Care – Residential Treatment Flyer</title>
<link href="https://fonts.googleapis.com/css2?family=Poppins:wght@500;600;700&family=Questrial&family=Arvo:wght@400;700&family=EB+Garamond:wght@400;500&display=swap" rel="stylesheet">
<style>
  :root {
    --stage: #8e8e8e;
    --paper: #ffffff;
    --charcoal: #4a4a4a;
    --charcoal-dark: #3a3a3a;
    --sky: #6fb6ea;
    --sky-soft: rgba(150, 200, 240, 0.75);
    --navy: #1b2380;
    --leaf: #2f9a3b;
    --ink: #3a3a3a;
    --muted: #5a5a5a;
    --link: #1f5fa8;
  }
  * { margin: 0; padding: 0; box-sizing: border-box; }
  html, body { width: 1200px; height: 1200px; overflow: hidden; background: var(--stage); }
  .flyer {
    position: absolute; left: 160px; top: 30px;
    width: 880px; height: 1140px;
    background: var(--paper); overflow: hidden;
    font-family: "Questrial", sans-serif;
    box-shadow: 0 6px 20px rgba(0,0,0,.25);
  }
  .flyer > * { position: absolute; }
  .room-photo {
    left: 0; top: 470px; width: 880px; height: 670px;
    background: linear-gradient(160deg, #e4e7ea 0%, #f4f5f6 45%, #eceeef 100%);
  }
  .shapes { left: 0; top: 0; width: 880px; height: 1140px; }
  .hero-photo {
    left: 0; top: 0; width: 340px; height: 580px;
    clip-path: path('M0 0 H250 C305 0 335 40 335 110 V390 C335 430 310 460 272 472 C250 500 230 530 205 552 V580 H0 Z');
    background: linear-gradient(180deg, #6c7075 0%, #8a8f96 35%, #b9c0c8 60%, #c9a6a0 100%);
  }
  .brand {
    left: 560px; top: 118px; display: flex; align-items: center; gap: 12px;
    font-family: "Poppins", sans-serif; font-weight: 700; font-size: 30px; color: var(--navy);
  }
  .brand-dot { width: 22px; height: 22px; border-radius: 50%; background: var(--navy); }
  .headline {
    right: 55px; top: 270px; text-align: right; color: #fff;
    font-family: "Poppins", sans-serif; font-weight: 700; line-height: 1;
    text-shadow: 0 0 3px var(--charcoal-dark), 2px 2px 0 var(--charcoal-dark);
  }
  .headline-state { font-size: 56px; letter-spacing: -1px; }
  .headline-sub { font-size: 23px; margin-top: 10px; }
  .headline-sub + .headline-sub { margin-top: 12px; }
  .lead {
    right: 55px; top: 408px; text-align: right; white-space: nowrap;
    color: #fff; font-size: 17.5px; line-height: 26px; letter-spacing: .1px;
  }
  .rule { left: 580px; top: 488px; width: 245px; height: 1px; background: #9aa; }
  .stat {
    right: 55px; top: 497px; text-align: right; white-space: nowrap;
    color: #fff; font-size: 13.5px; line-height: 25px; letter-spacing: -.2px;
  }
  .tagline {
    left: 218px; top: 560px; color: #fff;
    font-family: "Poppins", sans-serif; font-weight: 500; font-size: 34px; letter-spacing: -.5px;
    text-shadow: 0 0 3px var(--charcoal-dark), 2px 2px 0 var(--charcoal-dark);
  }
  .section-title { font-weight: 400; color: var(--ink); }
  .issues-title { left: 66px; top: 650px; font-size: 21px; letter-spacing: .3px; }
  .issues {
    left: 41px; top: 687px; width: 388px; height: 176px;
    background: var(--sky-soft); border-radius: 8px; list-style: none;
    padding: 16px 0 0 28px;
  }
  .issues li {
    display: flex; align-items: center; gap: 18px; height: 39.5px;
    font-family: "Arvo", serif; font-size: 21px; color: var(--navy); letter-spacing: .3px;
  }
  .issues svg { width: 30px; height: 30px; flex: none; }
  .program-label {
    left: 41px; top: 872px; width: 379px; height: 33px;
    background: var(--charcoal); color: #fff; font-size: 18.5px;
    display: flex; align-items: center; justify-content: center; letter-spacing: .2px;
  }
  .contact { left: 74px; top: 912px; list-style: none; color: var(--ink); }
  .contact li { display: flex; align-items: flex-start; gap: 10px; font-size: 20px; line-height: 28px; margin-bottom: 8px; }
  .contact svg { width: 24px; height: 24px; flex: none; margin-top: 2px; }
  .contact .address { font-size: 19.5px; }
  .visit { left: 55px; top: 1051px; font-size: 14px; color: var(--link); }
  .web-pill {
    left: 41px; top: 1077px; width: 508px; height: 31px; border-radius: 16px;
    background: var(--charcoal); color: #fff; box-shadow: 0 3px 4px rgba(0,0,0,.3);
    font-family: "Poppins", sans-serif; font-weight: 700; font-size: 20px; letter-spacing: 6px;
    display: flex; align-items: center; justify-content: center;
  }
  .why-title { left: 454px; top: 652px; font-family: "Arvo", serif; font-size: 20px; }
  .why-title strong { font-weight: 700; }
  .reasons { left: 460px; top: 692px; width: 375px; }
  .reason h3 {
    font-family: "EB Garamond", serif; font-weight: 500; font-size: 15.5px;
    color: var(--leaf); letter-spacing: .4px; margin-bottom: 8px;
  }
  .reason p {
    font-family: "EB Garamond", serif; font-size: 12.9px; line-height: 13.5px;
    color: var(--muted); margin-bottom: 10px;
  }
</style>
</head>
<body>
<main class="flyer">
  <div class="room-photo" role="img" aria-label="Faded photo of a bright, calm treatment center lounge"></div>

  <svg class="shapes" viewBox="0 0 880 1140" aria-hidden="true">
    <path d="M0 0 H880 V545 C700 560 520 605 340 605 C210 605 90 570 0 540 Z" fill="var(--charcoal)"/>
    <path d="M331 0 H880 V378 C720 345 560 260 460 160 C400 100 355 45 331 0 Z" fill="var(--paper)"/>
    <path d="M242 0 H331 C355 45 400 100 460 160 C560 260 720 345 880 378 V360 C700 330 520 230 420 140 C330 60 275 25 242 0 Z" fill="var(--sky)"/>
    <path d="M880 540 V588 C720 612 560 636 400 632 C340 630 300 620 270 608 C330 612 380 612 420 608 C580 600 730 575 880 540 Z" fill="var(--sky)"/>
    <path d="M470 1140 C600 1085 760 1045 880 1018 V1140 Z" fill="var(--charcoal)"/>
    <path d="M560 1140 C680 1108 790 1088 880 1080 V1140 Z" fill="var(--sky)"/>
  </svg>

  <div class="hero-photo" role="img" aria-label="Photo of a smiling program graduate holding his certificate of completion"></div>

  <div class="brand"><span class="brand-dot"></span>Morval Care</div>

  <h1 class="headline">
    <div class="headline-state">KENTUCKYS</div>
    <div class="headline-sub">LEADING DRUG &amp; ALCOHOL</div>
    <div class="headline-sub">ADDICTION TREATMENT</div>
  </h1>

  <p class="lead">PROVIDING THE HIGHEST LEVEL OF REHAB SERVICES<br>FOR PATIENTS DIAGNOSED WITH ALCHOHOL OR<br>OTHER DRUG OR SUBSTANCE ADDICTION.</p>
  <div class="rule"></div>
  <p class="stat">94% of those suffering from substance use disorder stay in active addiction without an<br>intervention. We offer the most effective and comfortable treatment that leads to success.</p>

  <h2 class="tagline">ADDICTION TREATMENT THAT WORKS</h2>

  <h2 class="section-title issues-title">WHAT ISSUES CAN BE TREATED?</h2>
  <ul class="issues">
    <li>
      <svg viewBox="0 0 30 30"><g transform="rotate(40 15 15)" fill="var(--navy)"><rect x="12" y="2" width="6" height="8" rx="1"/><rect x="8" y="10" width="14" height="18" rx="3"/><rect x="10" y="15" width="10" height="6" fill="#cfe4f7"/></g></svg>
      ALCOHOLISM
    </li>
    <li>
      <svg viewBox="0 0 30 30" fill="none" stroke="var(--navy)" stroke-width="2.4" stroke-linecap="round"><path d="M4 26 L9 21"/><rect x="9" y="9" width="7" height="16" rx="1" transform="rotate(45 12.5 17)"/><path d="M19 11 L25 5 M22 3 L27 8"/></svg>
      DRUG ADDICTION
    </li>
    <li>
      <svg viewBox="0 0 30 30" fill="var(--navy)"><rect x="2" y="8" width="12" height="18" rx="6" transform="rotate(-30 8 17)"/><circle cx="22" cy="18" r="7"/></svg>
      MEDICATION ADDICTION
    </li>
    <li>
      <svg viewBox="0 0 30 30" fill="none" stroke="var(--navy)" stroke-width="2"><path d="M9 28 V21 C5 18 4 14 5 10 C7 4 13 2 18 3 C24 5 26 10 25 14 L27 18 L24 19 V23 H19 V28"/><circle cx="15" cy="12" r="4"/></svg>
      BEHAVIORAL HEALTH
    </li>
  </ul>

  <div class="program-label">RESIDENTIAL/INPATIENT TREATMENT</div>

  <ul class="contact">
    <li>
      <svg viewBox="0 0 24 24"><circle cx="12" cy="12" r="12" fill="var(--sky)"/><path d="M8 6 L10 6 L11 9 L9.5 10.3 C10.3 12 11.8 13.6 13.7 14.5 L15 13 L18 14 V16 C18 17 17 18 16 18 C10.5 17.5 6.5 13.5 6 8 C6 7 7 6 8 6 Z" fill="#fff"/></svg>
      859-555-0142
    </li>
    <li>
      <svg viewBox="0 0 24 24"><circle cx="12" cy="12" r="12" fill="var(--sky)"/><rect x="6" y="8" width="12" height="9" rx="1" fill="#fff"/><path d="M6.5 8.5 L12 13 L17.5 8.5" fill="none" stroke="var(--sky)" stroke-width="1.4"/></svg>
      ADMISSIONS@MORVALCARE.COM
    </li>
    <li class="address">
      <svg viewBox="0 0 24 24"><path d="M12 2 C7.5 2 5 5.2 5 8.8 C5 14 12 22 12 22 C12 22 19 14 19 8.8 C19 5.2 16.5 2 12 2 Z" fill="var(--sky)"/><circle cx="12" cy="9" r="3" fill="#fff"/></svg>
      <span>2140 Meadow Ridge Rd, Richmond<br>&nbsp;KY 40475, United States</span>
    </li>
  </ul>

  <p class="visit">Visit us online for more information</p>
  <div class="web-pill">www.morvalcare.org</div>

  <h2 class="section-title why-title">WHY <strong>TREATMENT HERE</strong> WORKS</h2>
  <div class="reasons">
    <section class="reason">
      <h3>1. EVIDENCE BASED TREATMENT</h3>
      <p>We use evidence-based treatment that has been scientifically tested and proven to produce positive results. Ranging from cognitive behaviour therapy to dialectical therapy, we do what it takes to make you healthy.</p>
    </section>
    <section class="reason">
      <h3>2. INDIVIDUALIZED</h3>
      <p>You deserve individualized attention from experienced professionals who actually care. Our reputation, small case load and success rates mean you are given the best treatment from leading experts.</p>
    </section>
    <section class="reason">
      <h3>3. TELEMEDICINE</h3>
      <p>Morval Care is offering aspects of its treatment program via tele-health services to meet the need of clients seeking treatment from the convenience of their homes.</p>
    </section>
    <section class="reason">
      <h3>4. MEDICATION ASSISTED TREATMENT</h3>
      <p>Medication assisted treatment helps to relieve withdrawal symptoms and cravings which makes going clean easier. We treat addiction with FDA-approved medicines to help you focus on your recovery. We prescribe medicines such as Renavox (a treatment combining buprenorphine and naloxone), Naltrexa (a naltrexone treatment), and Bupreva (a buprenorphine treatment)</p>
    </section>
  </div>
</main>
</body>
</html>
```